Website Redesign for a Bar Association

Design a user-friendly website that promotes the most important content and drives user engagement. Directional site map (navigation & content flow) document attached.

Existing Website: http://brightfieldlaw.org/

Competitive Site Inspiration:
https://www.tarvenlaw.org
https://www.pqlaw.org

Must use one of the following Pagecraft themes:
https://zolaskins.com/lite/?theme=journal_lite
https://preview.kavrolayouts.com/?demo=swiftpress

Industry/Entity Type

Legal

Font styles to use
Serif
Sans Serif

Colors
0355a3
f37122

Requirements
Must have
• HLS Logo

```html
<!DOCTYPE html>
<html lang="en">
<head>
<meta charset="utf-8">
<title>Contact Us – Harbor Law Society</title>
<link rel="stylesheet" href="https://fonts.googleapis.com/css2?family=Lato:wght@400;700&family=Roboto+Slab:wght@500;700&display=swap">
<style>
:root{
  --navy:#2b3a5c;
  --navy-deep:#2e3c5e;
  --orange:#f06000;
  --field:#f2f2f2;
  --field-line:#e2e2e2;
  --text:#555b66;
  --bar:#8fbbd3;
  --white:#ffffff;
}
*{box-sizing:border-box;margin:0;padding:0}
html,body{width:835px;height:1200px;overflow:hidden}
body{position:relative;font-family:"Lato",sans-serif;color:var(--text)}
.city-backdrop{position:absolute;inset:0;background:linear-gradient(180deg,#4a5573 0%,#3b4560 35%,#2d3550 70%,#5a4a44 100%)}
.page{position:absolute;left:78px;top:0;width:680px;height:1127px;background:var(--white)}
.abs{position:absolute}
.brand{display:flex;align-items:center;gap:8px}
.brand-mark{width:30px;height:30px;background:var(--navy)}
.brand-name{font-family:"Lato",sans-serif;font-weight:700;font-size:15px;line-height:1.05;color:var(--navy);letter-spacing:.5px}
.btn{display:flex;align-items:center;justify-content:center;color:var(--white);font-weight:700;font-size:10.5px;border-radius:2px}
.btn-donate{left:468px;top:30px;width:77px;height:28px;background:var(--orange)}
.btn-login{left:558px;top:30px;width:108px;height:28px;background:var(--navy);gap:5px}
.nav{left:0;top:89px;width:680px;height:30px;background:var(--orange);display:flex}
.nav a{color:var(--white);text-decoration:none;font-weight:700;font-size:10.7px;display:flex;align-items:center;padding:0 14.5px}
.nav a.active{background:var(--navy);margin-left:auto;padding:0 15px;width:97px}
.hero{left:0;top:119px;width:680px;height:178px;background:linear-gradient(180deg,#c98a6a 0%,#3a5a8c 40%,#243a63 75%,#7a4a30 100%);display:flex;align-items:center;justify-content:center}
.hero h1{font-family:"Roboto Slab",serif;font-weight:700;font-size:30px;color:var(--white)}
.help-title{left:0;top:362px;width:680px;text-align:center;font-family:"Roboto Slab",serif;font-weight:700;font-size:22.5px;color:var(--navy)}
.info-label{font-weight:700;font-size:12.5px;color:var(--navy)}
.info-text{font-size:10px;line-height:15.5px;color:var(--text)}
.touch-title{left:32px;top:508px;font-family:"Roboto Slab",serif;font-weight:700;font-size:17px;color:var(--navy)}
.touch-rule{left:32px;top:533px;width:44px;height:2px;background:var(--orange)}
.touch-sub{left:32px;top:546px;font-size:10.5px}
.field{left:32px;width:281px;background:var(--field);border:1px solid var(--field-line);font-size:8px;color:#666;padding:0 10px;display:flex;align-items:center}
.field-area{align-items:flex-start;padding-top:10px}
.submit{left:32px;top:774px;width:281px;height:28px;background:var(--orange);color:var(--white);font-weight:700;font-size:12px;display:flex;align-items:center;justify-content:center;border-radius:2px}
.map{left:350px;top:504px;width:297px;height:297px;border:3px solid #f4f4f4;background:linear-gradient(135deg,#ececec,#e4e1d8)}
.footer{left:0;top:887px;width:680px;height:204px;background:var(--navy-deep);color:var(--white)}
.footer-about{left:25px;top:89px;width:192px;font-size:9px;line-height:13.8px}
.footer-col h3{font-size:12px;font-weight:700;margin-bottom:9px}
.footer-col li{list-style:none;font-size:9px;line-height:17.9px}
.bottom-bar{left:0;top:1091px;width:680px;height:36px;background:var(--bar);color:var(--white);font-size:10px}
.social{position:absolute;top:7px;width:20px;height:20px;border:1.3px solid var(--white);border-radius:50%}
</style>
</head>
<body>
<div class="city-backdrop" role="img" aria-label="Night aerial photo of a downtown skyline"></div>
<div class="page">
  <header>
    <div class="abs brand" style="left:14px;top:28px">
      <span class="brand-mark"></span>
      <span class="brand-name">HARBOR LAW<br>SOCIETY</span>
    </div>
    <div class="abs btn btn-donate">DONATE</div>
    <div class="abs btn btn-login">
      <svg width="10" height="9" viewBox="0 0 10 9"><path d="M5 9 0.8 4.8A2.4 2.4 0 0 1 5 1.4 2.4 2.4 0 0 1 9.2 4.8Z" fill="#fff"/></svg>
      MEMBER LOGIN
    </div>
    <nav class="abs nav">
      <a>Home</a><a>Join Now!</a><a>About the HLS</a><a>Committees</a><a>Harbor Law Foundation</a><a>Resources</a><a class="active">Contact Us</a>
    </nav>
  </header>
  <section class="abs hero" role="img" aria-label="City skyline at dusk overlaid with a world map and connection lines">
    <h1>Contact Us</h1>
  </section>

  <h2 class="abs help-title">How Can we Help You</h2>

  <svg class="abs" style="left:44px;top:421px" width="36" height="38" viewBox="0 0 36 38" fill="none" stroke="#f06000" stroke-width="2"><path d="M18 28C10 19 8 15 8 11a10 10 0 0 1 20 0c0 4-2 8-10 17Z"/><circle cx="18" cy="11" r="4"/><path d="M10 26 3 36h30l-7-10M3 36h30"/></svg>
  <div class="abs" style="left:93px;top:417px"><div class="info-label">LOCATION:</div><div class="info-text">210 Calloway Ave, Suite 400-218 Rivermont,<br>MI 48390</div></div>

  <svg class="abs" style="left:306px;top:418px" width="40" height="40" viewBox="0 0 40 40" fill="none" stroke="#f06000" stroke-width="1.6"><path d="M2 16 20 3l18 13v22H2Z"/><path d="M2 16l18 13 18-13M2 38l14-12M38 38 24 26"/><path d="M11 14h18M11 18h14"/></svg>
  <div class="abs" style="left:358px;top:425px"><div class="info-label">EMAIL:</div><div class="info-text">info@brightfieldlaw.org</div></div>

  <svg class="abs" style="left:518px;top:422px" width="34" height="34" viewBox="0 0 34 34" fill="none" stroke="#f06000" stroke-width="2"><path d="M8 3l5 7-3 4c2 4 6 8 10 10l4-3 7 5-3 5C17 30 4 17 3 7Z"/><path d="M20 7a8 8 0 0 1 7 7M20 2a13 13 0 0 1 12 12"/></svg>
  <div class="abs" style="left:567px;top:425px"><div class="info-label">PHONE:</div><div class="info-text">(555) 314-0872</div></div>

  <h2 class="abs touch-title">GET IN TOUCH</h2>
  <div class="abs touch-rule"></div>
  <p class="abs touch-sub">Reach out to us for any inquiry</p>
  <div class="abs field" style="top:578px;height:28px">First Name*</div>
  <div class="abs field" style="top:616px;height:28px">Last Name*</div>
  <div class="abs field" style="top:655px;height:28px">Your E-mail Address*</div>
  <div class="abs field field-area" style="top:693px;height:58px">How can we help you?*</div>
  <div class="abs submit">CONTACT US NOW</div>

  <div class="abs map" role="img" aria-label="Street map showing the society's office location with a marker"></div>

  <footer class="abs footer">
    <div class="abs brand" style="left:25px;top:26px">
      <span class="brand-mark" style="background:var(--white)"></span>
      <span class="brand-name" style="color:var(--white);font-size:13px">HARBOR LAW<br>SOCIETY</span>
    </div>
    <p class="abs footer-about">The Harbor Law Society was established by a number of African-American attorneys during the 1930's. It was organized to coordinate the energies and talents of the increasing number of African-Americans admitted to practice throughout Michigan.</p>
    <div class="abs footer-col" style="left:269px;top:53px"><h3>Company</h3><ul><li>About</li><li>Scholarships</li><li>Community Resources</li><li>News and Events</li><li>Contact Us</li></ul></div>
    <div class="abs footer-col" style="left:415px;top:53px"><h3>Member Resources</h3><ul><li>Member Directory</li><li>Get Involved</li><li>Jobs</li><li>Member</li><li>On the Move</li></ul></div>
    <div class="abs footer-col" style="left:558px;top:53px"><h3>Programs</h3><ul><li>Law School Pipeline</li><li>Summer Clerkship</li><li>Judicial Externship</li><li>Pipeline Programs</li><li>Minority Bar Passage</li></ul></div>
  </footer>
  <div class="abs bottom-bar">
    <span class="abs" style="left:25px;top:10px">© Copyright 2020 brightfieldlaw. All Rights Reserved</span>
    <span class="social" style="left:548px" aria-label="Social link"></span>
    <span class="social" style="left:575px" aria-label="Social link"></span>
    <span class="social" style="left:601px" aria-label="Social link"></span>
    <span class="social" style="left:628px" aria-label="Social link"></span>
  </div>
</div>
</body>
</html>
```